CD/Music Release Cover titled Bring On The Porch Night

We're an Appalachian old time string band located in Richmond, Virginia, USA. Our instruments are banjo, mandolin, fiddle, guitar, and bass. We take music seriously but we are also five good friends playing to have fun. After all, a lot of what we are playing is dance music. Or songs about moonshine. A murder ballad but you can dance to it.
Our CD title is "Bring On The Porch Night." It reflects both our longing to get out from under the shadow of 2020 (we recorded the CD early in the year) and our general philosophy of having a good time playing. For the CD cover art, we envision a chicken-- it represents an inside joke, as well as the rural roots of some of the music we play. We're thinking a simple, cleanly drawn chicken, with a little sass. A jaunty chicken. A party chicken, if you will. But a cool one. Not too silly A cool jaunty party chicken. Or perhaps representing the band with 3 roosters playing mandolin, banjo and upright bass and 2 chickens playing fiddle and guitar. See photo of band. Also see WillowLaneDrifters.com and https://www.facebook.com/WillowLaneDrifters for more information about us.
Updates

We are new to using this service, and we didn't realize that our feedback would result in additional design ideas. Thank you for your patience and for working with us.

Target Market(s)

Fans (whether they know it or not) of Appalachian Stringband Music.

Font styles to use
Serif

Requirements
Must have
• If instruments are included in design, they would need to be as close as possible to our instruments shown in band photo.

Include name of band and cd name:
Willow Lane Drifters
Bring On The Porch Night

```html
<!DOCTYPE html>
<html lang="en">
<head>
<meta charset="utf-8">
<title>Willow Lane Drifters – Bring On The Porch Night</title>
<link rel="stylesheet" href="https://fonts.googleapis.com/css2?family=Sancreek&family=Rye&display=swap">
<style>
  :root {
    --sky-top: #3a2a1c;
    --sky-glow: #b86a1c;
    --field: #6e5630;
    --ground: #2a2016;
    --bird-light: #efe6d2;
    --bird-shade: #b9a98a;
    --title-yellow: #eed85a;
    --title-shadow: #24160c;
  }
  html, body {
    margin: 0;
    padding: 0;
    overflow: hidden;
    background: var(--ground);
  }
  .cover {
    position: relative;
    width: 1200px;
    height: 1200px;
    overflow: hidden;
  }
  .cover-art {
    position: absolute;
    inset: 0;
    display: block;
  }
  .band-name {
    font-family: "Sancreek", "Rye", serif;
    fill: var(--title-yellow);
    stroke: var(--title-shadow);
    stroke-width: 14px;
    paint-order: stroke fill;
    stroke-linejoin: round;
  }
  .release-title {
    font-family: "Rye", "Sancreek", serif;
    fill: var(--title-yellow);
    stroke: var(--title-shadow);
    stroke-width: 12px;
    paint-order: stroke fill;
    stroke-linejoin: round;
  }
</style>
</head>
<body>
<main class="cover">
  <svg class="cover-art" width="1200" height="1200" viewBox="0 0 1200 1200" xmlns="http://www.w3.org/2000/svg">
    <defs>
      <linearGradient id="sceneTone" x1="0" y1="0" x2="0" y2="1">
        <stop offset="0" stop-color="var(--sky-top)"/>
        <stop offset="0.3" stop-color="var(--sky-glow)"/>
        <stop offset="0.55" stop-color="var(--field)"/>
        <stop offset="1" stop-color="var(--ground)"/>
      </linearGradient>
      <radialGradient id="birdTone" cx="0.5" cy="0.45" r="0.6">
        <stop offset="0" stop-color="var(--bird-light)"/>
        <stop offset="1" stop-color="var(--bird-shade)"/>
      </radialGradient>
      <filter id="titleDrop" x="-10%" y="-10%" width="130%" height="130%">
        <feDropShadow dx="-10" dy="10" stdDeviation="2" flood-color="#1a0f08" flood-opacity="0.85"/>
      </filter>
    </defs>

    <rect class="scene-backdrop" x="0" y="0" width="1200" height="1200" fill="url(#sceneTone)"
          role="img" aria-label="Painted rural scene: amber stormy sunset sky over dry fields with a weathered wooden fence and gate"/>

    <rect class="mascot-illustration" x="700" y="120" width="440" height="500" rx="60" fill="url(#birdTone)" opacity="0.9"
          role="img" aria-label="White chicken in a cowboy hat standing on a fence rail, playing a five-string banjo"/>

    <g class="band-name-block" filter="url(#titleDrop)">
      <text class="band-name" x="60" y="375" font-size="300" textLength="540" lengthAdjust="spacingAndGlyphs">WILLOW</text>
      <text class="band-name" x="55" y="645" font-size="300" textLength="470" lengthAdjust="spacingAndGlyphs">LANE</text>
      <text class="band-name" x="55" y="925" font-size="300" textLength="905" lengthAdjust="spacingAndGlyphs">DRIFTERS</text>
    </g>

    <text class="release-title" x="65" y="1112" font-size="78" textLength="1020" lengthAdjust="spacingAndGlyphs" filter="url(#titleDrop)">BRING ON THE PORCH NIGHT</text>
  </svg>
</main>
</body>
</html>
```